Promo Flyer to put in prize bags at carnival

I am owner of Willow & Pike Hair Salon located in Gahanna, OH. I’m sponsoring a community carnival when I will be putting flyers in all attendees prize bags. This flyer will communicate details of my salon on one side (picture of me, logo, description of business, address, website, email, phone #) and the other side will showcase and a 50% discount for first time customers. Flyer can be 5” x 7” or greater

Side 1 details:
-Logo will be attached to this brief
-picture of me will be attached to this brief
-address: 2641 W. Brockton Ave, Suite 17, Gahanna, OH, 43230
-website: wphairstudio.example
-email: Dorian.blake@wphairstudio.example
-phone: 614-55-GOWPS (46977)

Side 2 details:
-‘Guess what? You get 50% off your 1st service at Willow & Pike Hair Salon.’
-‘Expires 7/31/2018’
-Hair | Fashion | Photography
-Visit wphairstudio.example to book your service
-must present this flyer at time of service to receive discount

Industry/Entity Type

Hair And Beauty

Font styles to use
Other font styles liked:
• Inoxida

Colors
3176b5
000000
ffffff

Requirements
Must have
• 2 sides
• Color scheme to match logo

```html
<!DOCTYPE html>
<html lang="en">
<head>
<meta charset="utf-8">
<title>Willow &amp; Pike Hair Salon – Promo Flyer</title>
<link rel="stylesheet" href="https://fonts.googleapis.com/css2?family=Merriweather:ital,wght@0,400;0,700;1,400;1,700&display=swap">
<style>
  :root {
    --ink: #151515;
    --paper: #ffffff;
    --page: #ffffff;
    --brand-blue: #5381b4;
    --accent-blue: #4f7fbb;
    --icon-blue: #4ea6dd;
    --gold: #e6a623;
    --text-dark: #1d1d1d;
  }
  * { box-sizing: border-box; margin: 0; padding: 0; }
  html, body {
    width: 1200px; height: 1200px; overflow: hidden;
    background: var(--page);
    font-family: "Merriweather", Georgia, serif;
  }
  .flyer {
    position: absolute; left: 230px; width: 739px; height: 527px;
    overflow: hidden;
    box-shadow: 0 6px 14px rgba(0,0,0,0.22);
  }
  .flyer--front { top: 50px; background: var(--ink); color: var(--paper); }
  .flyer--back { top: 622px; background: var(--paper); color: var(--text-dark); }

  .portrait {
    position: absolute; left: 386px; top: 0; width: 353px; height: 527px;
    background:
      linear-gradient(90deg, var(--ink) 0%, rgba(21,21,21,0) 30%),
      linear-gradient(160deg, #8b8680 0%, #5c5955 35%, #2f4a55 60%, #1f3a48 100%);
  }

  .brand {
    position: absolute; left: 0; width: 388px; text-align: center;
  }
  .flyer--front .brand { top: 80px; }
  .flyer--back .brand { left: 0; width: 739px; top: 95px; }
  .brand__dot {
    display: block; width: 34px; height: 34px; border-radius: 50%;
    background: var(--gold); margin: 0 auto 18px;
  }
  .brand__name {
    font-size: 38px; font-weight: 700; letter-spacing: 0.5px;
  }

  .contact { position: absolute; left: 38px; top: 268px; list-style: none; }
  .contact__item {
    display: flex; align-items: flex-start; gap: 14px;
    font-size: 17px; font-weight: 700; line-height: 26px;
    margin-bottom: 24px;
  }
  .contact__icon { width: 24px; height: 26px; flex: none; }
  .contact__icon svg { width: 24px; height: 26px; fill: var(--icon-blue); }
  .contact__item--address .contact__icon { margin-top: 12px; }

  .web-band {
    position: absolute; left: 0; top: 447px; width: 358px; height: 41px;
    background: var(--paper); color: var(--text-dark);
    border-radius: 0 0 40px 0;
    font-size: 17px; line-height: 41px; padding-left: 76px;
  }

  .offer {
    position: absolute; left: 0; width: 739px; top: 256px;
    text-align: center; font-size: 24px; line-height: 35px;
  }
  .offer__highlight { color: var(--accent-blue); font-style: italic; }
  .details {
    position: absolute; left: 65px; width: 609px; top: 342px;
    display: flex; align-items: center; gap: 14px;
    font-size: 21px;
  }
  .details__rule { flex: 1; height: 1px; background: var(--text-dark); }
  .details__expiry { font-style: italic; font-weight: 700; }
  .booking {
    position: absolute; left: 0; width: 739px; top: 390px;
    text-align: center; font-size: 21px;
  }
  .booking__site { font-style: italic; font-weight: 700; }
  .terms-band {
    position: absolute; left: 0; top: 443px; width: 739px; height: 50px;
    background: var(--brand-blue); color: var(--paper);
    text-align: center; line-height: 50px;
    font-size: 20px; font-weight: 700;
  }
</style>
</head>
<body>

<section class="flyer flyer--front">
  <div class="portrait" role="img" aria-label="Photo of the salon owner in a teal suit and sunglasses on a city street"></div>

  <div class="brand">
    <span class="brand__dot"></span>
    <div class="brand__name">Willow &amp; Pike</div>
  </div>

  <ul class="contact">
    <li class="contact__item contact__item--address">
      <span class="contact__icon"><svg viewBox="0 0 24 26"><path d="M12 1C7.6 1 4 4.5 4 8.9 4 14.8 12 25 12 25s8-10.2 8-16.1C20 4.5 16.4 1 12 1zm0 11a3.3 3.3 0 1 1 0-6.6 3.3 3.3 0 0 1 0 6.6z"/></svg></span>
      <span>2641 W. Brockton Ave, Suite 17,<br>Gahanna, OH, 43230</span>
    </li>
    <li class="contact__item">
      <span class="contact__icon"><svg viewBox="0 0 24 26"><path d="M1 7h22v2.2l-11 6.5L1 9.2z"/><path d="M1 11.5l11 6.5 11-6.5V21H1z"/></svg></span>
      <span>dorian.blake@wphairstudio.example</span>
    </li>
    <li class="contact__item">
      <span class="contact__icon"><svg viewBox="0 0 24 26"><path d="M6.5 3.5l3.2 4.3-2 2.6c1.3 3 3.6 5.4 6.5 6.8l2.3-2 4.4 3.1-1.7 4.2C10.8 22 3.6 13.2 2.6 5.3z"/></svg></span>
      <span>614-55-GOWPS (46977)</span>
    </li>
  </ul>

  <div class="web-band">www.wphairstudio.example</div>
</section>

<section class="flyer flyer--back">
  <div class="brand">
    <span class="brand__dot"></span>
    <div class="brand__name">Willow &amp; Pike</div>
  </div>

  <p class="offer">Guess what? You get <span class="offer__highlight">50% off</span> your 1st service<br>at Willow &amp; Pike Hair Salon.</p>

  <div class="details">
    <span class="details__rule"></span>
    <span><span class="details__expiry">Expires 7/31/2018</span> · Hair | Fashion | Photography</span>
    <span class="details__rule"></span>
  </div>

  <p class="booking">Visit <span class="booking__site">wphairstudio.example</span> to book your service</p>

  <div class="terms-band">Must present this flyer at time of service to receive discount</div>
</section>

</body>
</html>
```